Vesk Architecture

We are a architectural design and build company working between scales 1/1000 to 1/1 we want people to understand our difference from our design experience and quality.we build hotels restourants and office spaces.Our company name is Vesk architecture to mind sustainability.

We want to write our adress phone and work spesifications on the card and we want our logo as backround.

Ps:you could find the logo adress and phone box numbers from the web:www.veskmimarlik-ornek.com

Target Market(s)

Who looks for experts.

Industry/Entity Type

Architecture

Requirements
Must have
• Design is over everything.
Should not have
• we don want it to be colorfull

```html
<!DOCTYPE html>
<html lang="tr">
<head>
<meta charset="utf-8">
<title>Vesk Architecture – Business Card</title>
<link rel="stylesheet" href="https://fonts.googleapis.com/css2?family=PT+Serif&family=Montserrat:wght@500&display=swap">
<style>
  :root{
    --page:#ffffff;
    --card-light:#fbfbfb;
    --card-dark:#e4e4e4;
    --brown:#8b2a16;
    --brown-deep:#6e1c0c;
    --peach:#fbd3a6;
    --cream:#fde6c8;
    --ink:#161616;
  }
  *{margin:0;padding:0;box-sizing:border-box}
  html,body{width:1200px;height:900px;overflow:hidden;background:var(--page)}
  .canvas{position:relative;width:1200px;height:900px}

  .card{position:absolute;overflow:hidden;
    background:linear-gradient(160deg,var(--card-light) 0%,#f1f1f1 55%,var(--card-dark) 100%);
    box-shadow:0 18px 22px -14px rgba(0,0,0,.28)}

  /* back side */
  .card--back{left:356px;top:28px;width:660px;height:362px}
  .ornament{position:absolute;display:block}
  .ornament--top{left:0;top:0;width:660px;height:112px}
  .contact{position:absolute;left:20px;top:114px;font-family:"PT Serif",serif;color:var(--brown)}
  .contact__street{font-size:28px;word-spacing:4px;letter-spacing:.3px;margin-bottom:6px}
  .contact__line{font-size:21px;line-height:29px}
  .contact__line span+span{margin-left:22px}
  .wordmark{position:absolute;font-family:"PT Serif",serif;color:var(--ink);font-weight:400;line-height:1}
  .card--back .wordmark{left:482px;top:218px;text-align:left}
  .card--back .wordmark__name{font-size:68px;letter-spacing:1px}
  .card--back .wordmark__sub{font-size:19px;letter-spacing:1px;margin-top:4px}
  .web-band{position:absolute;left:0;bottom:0;width:100%;height:30px;background:var(--peach);
    font-family:"PT Serif",serif;color:var(--brown);font-size:18px;line-height:30px;
    letter-spacing:15px;padding-left:26px;white-space:nowrap}

  /* front side */
  .card--front{left:200px;top:486px;width:664px;height:404px}
  .card--front .wordmark{left:34px;top:20px}
  .card--front .wordmark__name{font-size:176px;letter-spacing:2px}
  .card--front .wordmark__sub{font-size:40px;letter-spacing:2px;margin-top:6px}
  .ornament--corner{right:0;bottom:0;width:310px;height:236px}
</style>
</head>
<body>
<main class="canvas">

  <section class="card card--back" aria-label="Business card, back">
    <svg class="ornament ornament--top" viewBox="0 0 660 112" role="img" aria-label="Flowing floral flourish ornament in brown and peach" preserveAspectRatio="none">
      <defs>
        <linearGradient id="topFlourish" x1="0" y1="0" x2="1" y2="0">
          <stop offset="0" stop-color="#8b2a16"/>
          <stop offset=".45" stop-color="#fbd3a6"/>
          <stop offset="1" stop-color="#a13a1f"/>
        </linearGradient>
      </defs>
      <path d="M0 0H660V30C560 40 470 70 380 84C280 100 170 70 90 80C50 85 20 96 0 100Z" fill="url(#topFlourish)" opacity=".85"/>
    </svg>

    <address class="contact">
      <p class="contact__street">Ardic Mah . Lale Cad . Papatya Sok .</p>
      <p class="contact__line">No :  7 Lale Kadikoy / Istanbul</p>
      <p class="contact__line"><span>T. 0216 000 41 52</span><span>F . 0216 000 41 53</span></p>
      <p class="contact__line">E - mail : veskmimarlik@ornek-posta.com</p>
    </address>

    <div class="wordmark">
      <div class="wordmark__name">vesk</div>
      <div class="wordmark__sub">MİMARLIK</div>
    </div>

    <div class="web-band">www.veskmimarlik-ornek.com</div>
  </section>

  <section class="card card--front" aria-label="Business card, front">
    <div class="wordmark">
      <div class="wordmark__name">vesk</div>
      <div class="wordmark__sub">MİMARLIK</div>
    </div>

    <svg class="ornament ornament--corner" viewBox="0 0 310 236" role="img" aria-label="Curling floral flourish ornament in brown and peach" preserveAspectRatio="none">
      <defs>
        <linearGradient id="cornerFlourish" x1="0" y1="1" x2="1" y2="0">
          <stop offset="0" stop-color="#8b2a16"/>
          <stop offset=".5" stop-color="#f6b98a"/>
          <stop offset="1" stop-color="#fde6c8"/>
        </linearGradient>
      </defs>
      <path d="M310 0V236H0C40 200 70 150 120 120C170 90 200 60 240 40C270 25 295 8 310 0Z" fill="url(#cornerFlourish)" opacity=".85"/>
    </svg>
  </section>

</main>
</body>
</html>
```